brochure for high-end senior living company

We need a new brochure that we can pass out to doctors and social workers so they would choose us over the competition.
quietharborgrove.com is our website that shows our colors and themes

we stand out over our competition due to our high quality of staff and our staff to resident ratio.
We are not afraid of difficult and complex care situations. Instead, we thrive on coordinating complexity.

We do all of this in a lovely setting that is luxurious and feels like home.

Target Market(s)

The families who make the decision are 60-70 years old. They are not not "rich" but they have saved well and usually have more than 1 million in assets.

Industry/Entity Type

Senior Living, Memory Care

Font styles to use
Serif

Colors
00AB8E
00BBA5
67D7C9
C6EFE9
E9F9F6
FFC000
F8CF3A
FAE287
FDF2CF
FEFAEE

Requirements
Must have
• When compromise is not an option...
Nice to have
• A difficult balance of beautiful and activities (happy people), but also communicating that we handle difficult and complex care.

```html
<!DOCTYPE html>
<html lang="en">
<head>
<meta charset="utf-8">
<title>Quiet Harbor Residential Assisted Living – Brochure Cover</title>
<link rel="stylesheet" href="https://fonts.googleapis.com/css2?family=Crimson+Text:ital,wght@0,400;0,600;1,400&family=Inter:wght@400;600&display=swap">
<style>
  :root {
    --teal-deep: #005a4f;
    --teal: #00ab8e;
    --teal-bright: #00bba5;
    --teal-soft: #67d7c9;
    --teal-mist: #c6efe9;
    --teal-wash: #e9f9f6;
    --gold: #f0b800;
    --gold-warm: #f8cf3a;
    --paper: #ffffff;
    --ink: #1c1c1c;
    --rule: #8a8a8a;
  }
  * { margin: 0; padding: 0; box-sizing: border-box; }
  html, body { width: 848px; height: 1200px; overflow: hidden; background: var(--paper); }
  .cover { position: relative; width: 848px; height: 1200px; background: var(--paper); font-family: "Inter", sans-serif; color: var(--ink); }

  .gold-tab { position: absolute; left: 640px; top: 0; width: 171px; height: 275px; background: var(--gold); }

  .brand { position: absolute; left: 60px; top: 118px; width: 536px; text-align: center; font-family: "Crimson Text", serif; }
  .brand-name { font-size: 64px; font-weight: 600; letter-spacing: 2px; text-transform: uppercase; line-height: 1; white-space: nowrap; color: var(--teal-deep); }
  .brand-rule { width: 490px; height: 2px; margin: 12px auto 0; background: var(--gold); }
  .brand-descriptor { margin-top: 14px; font-size: 34px; font-weight: 400; color: var(--ink); white-space: nowrap; }

  .hero-photo { position: absolute; left: 48px; top: 376px; width: 763px; height: 321px;
    background: linear-gradient(180deg, var(--teal-wash) 0%, var(--teal-wash) 30%, #e6d6a6 55%, #cdbd8e 78%, #6f8a55 100%); }

  .promise-line { position: absolute; left: 0; top: 718px; width: 848px; text-align: center; font-family: "Crimson Text", serif; font-style: italic; font-size: 28px; color: var(--teal); white-space: nowrap; }

  .headline-band { position: absolute; left: 0; top: 780px; width: 848px; height: 215px; background: var(--teal-deep); color: #fff; text-align: center; }
  .headline { margin-top: 28px; font-size: 48px; font-weight: 400; line-height: 62px; }
  .headline-sub { margin-top: 16px; font-size: 22px; font-weight: 400; color: var(--teal-mist); }

  .contact-strip { position: absolute; left: 60px; top: 1072px; width: 740px; }
  .contact-item { position: absolute; top: 0; }
  .contact-item.office { left: 0; }
  .contact-item.phone { left: 372px; }
  .contact-item.social { left: 645px; }
  .contact-label { font-size: 17px; font-weight: 600; color: var(--ink); white-space: nowrap; }
  .contact-detail { display: flex; align-items: center; gap: 12px; margin-top: 10px; font-size: 11px; white-space: nowrap; }
  .social-icons { display: flex; gap: 10px; margin-top: 9px; }
  .social-icons span { width: 21px; height: 21px; background: var(--gold); border-radius: 2px; }
  .contact-rule { position: absolute; left: 43px; top: 1130px; width: 762px; height: 1px; background: var(--rule); }
</style>
</head>
<body>
<main class="cover">
  <div class="gold-tab"></div>

  <header class="brand">
    <div class="brand-name">Quiet Harbor</div>
    <div class="brand-rule"></div>
    <div class="brand-descriptor">Residential Assisted Living</div>
  </header>

  <div class="hero-photo" role="img" aria-label="Photograph of a single-story cream and stone residential care home with a tiled roof, front walkway, young trees and a flagpole"></div>

  <p class="promise-line">When compromise is not an option...</p>

  <section class="headline-band">
    <h1 class="headline">The Perfect Balance of<br>Safety &amp; Warmth</h1>
    <p class="headline-sub">Professional &amp; Friendly Care in a Home Environment</p>
  </section>

  <footer class="contact-strip">
    <div class="contact-item office">
      <div class="contact-label">Local Office</div>
      <div class="contact-detail">
        <svg width="12" height="15" viewBox="0 0 12 15" aria-hidden="true"><path d="M6 0a6 6 0 0 0-6 6c0 4.5 6 9 6 9s6-4.5 6-9a6 6 0 0 0-6-6z" fill="#f0b800"/><circle cx="6" cy="6" r="2.2" fill="#fff"/></svg>
        <span>2240 Linden Park Rd, Fairbrook, CA 95410</span>
      </div>
    </div>
    <div class="contact-item phone">
      <div class="contact-label">Call Today</div>
      <div class="contact-detail">
        <svg width="14" height="14" viewBox="0 0 24 24" aria-hidden="true"><path d="M6.6 10.8a15.1 15.1 0 0 0 6.6 6.6l2.2-2.2a1 1 0 0 1 1-.25 11.4 11.4 0 0 0 3.6.57 1 1 0 0 1 1 1V20a1 1 0 0 1-1 1A17 17 0 0 1 3 4a1 1 0 0 1 1-1h3.5a1 1 0 0 1 1 1c0 1.25.2 2.45.57 3.57a1 1 0 0 1-.25 1z" fill="#f0b800"/></svg>
        <span>555-014-2738</span>
      </div>
    </div>
    <div class="contact-item social">
      <div class="contact-label">Follow Us</div>
      <div class="social-icons"><span></span><span></span><span></span></div>
    </div>
  </footer>
  <div class="contact-rule"></div>
</main>
</body>
</html>
```